Policy Manual in Education

I need the attached document to be put in a publishable format, with graphics a professional layout, and something that looks more like a professional report, etc. Use color samples from http://www.brvt-lo.com/ and www.kt7up.com, my company is Kt7up, we were hired to write the report and we also built the BRVT resource center http://www.brvt-lo.com/ .

Education

• Look and feel around NM. http://www.brvt-lo.com/ and www.kt7up.com

```html
<!DOCTYPE html>
<html lang="en">
<head>
<meta charset="utf-8">
<title>Kt7up – BRVT Educator Toolkit Layout</title>
<link href="https://fonts.googleapis.com/css2?family=Oswald:wght@300;400;500&family=Open+Sans:wght@400;600;700&family=Montserrat:wght@300;400&display=swap" rel="stylesheet">
<style>
:root{
  --board:#a4a4a4;
  --paper:#ffffff;
  --orange:#f26b2e;
  --amber:#f9a51b;
  --yellow:#f7c21b;
  --ink:#3a3a3a;
  --body:#5a5a5a;
  --muted:#8a8a8a;
  --slate:#5b5b5b;
  --label:#4e4e4e;
}
*{box-sizing:border-box;margin:0;padding:0}
html,body{width:794px;height:1200px;overflow:hidden;background:var(--board)}
body{position:relative;font-family:"Open Sans",sans-serif;color:var(--body)}
.page{position:absolute;width:234px;height:330px;background:var(--paper);overflow:hidden;box-shadow:0 1px 3px rgba(0,0,0,.25)}
.page::before{content:"";position:absolute;left:0;top:0;right:0;height:3px;background:linear-gradient(90deg,var(--orange),var(--amber))}
.page-label{position:absolute;width:234px;text-align:center;font-family:"Montserrat",sans-serif;font-weight:300;font-size:17px;letter-spacing:.5px;color:var(--label)}
.content{position:absolute;left:11px;right:11px;top:10px;bottom:22px;overflow:hidden}
.footer{position:absolute;left:11px;right:11px;bottom:7px;height:9px;border-top:.6px solid var(--amber);display:flex;align-items:flex-end;justify-content:space-between;font-size:3.6px;color:var(--muted)}
.footer .brand{font-weight:700;color:var(--orange);font-size:4.6px;display:flex;align-items:center;gap:1.5px}
.footer .brand i{width:3px;height:3px;background:var(--orange);display:block}
.footer .url{letter-spacing:1.4px}
p.t{font-size:3.2px;line-height:4.5px;margin-bottom:3px;color:var(--body)}
ul.b{list-style:none;margin:2px 0 4px}
ul.b li{font-size:3.2px;line-height:4.5px;padding-left:6px;position:relative;margin-bottom:2.5px}
ul.b li::before{content:"";position:absolute;left:1px;top:1.4px;width:1.8px;height:1.8px;border-radius:50%;background:var(--orange)}
ul.b.sub{margin-left:6px}
.bar{background:linear-gradient(90deg,var(--yellow),var(--amber));font-size:3.6px;font-weight:700;color:var(--ink);padding:2px 4px;margin:4px 0 4px;width:80%}
.callout{background:var(--orange);color:#fff;font-size:3.2px;line-height:4.5px;font-weight:600;padding:4px 5px;margin:4px -11px 5px}
.tag{display:inline-block;background:var(--orange);color:#fff;font-size:3.2px;font-weight:700;padding:1.2px 4px;margin:4px 0 3px}
.section{text-align:center;margin:8px 0 8px}
.section .kicker{font-family:"Oswald",sans-serif;font-size:8px;color:var(--orange);letter-spacing:.5px}
.section .dots{display:flex;justify-content:center;gap:1.5px;margin:1px 0 3px}
.section .dots i{width:1.6px;height:1.6px;border-radius:50%;background:var(--amber);display:block}
.section h2{font-family:"Oswald",sans-serif;font-weight:300;font-size:10.5px;line-height:12px;color:var(--orange)}
/* cover */
.cover .logo{position:absolute;left:11px;top:14px;font-family:"Open Sans",sans-serif;font-weight:400;font-size:16px;color:var(--slate);display:flex;align-items:center;gap:4px}
.cover .logo i{width:9px;height:9px;background:var(--orange);display:block}
.cover .tagline{position:absolute;left:26px;top:35px;font-size:3.2px;color:var(--muted);letter-spacing:.4px}
.cover .portrait{position:absolute;left:136px;top:3px;width:98px;height:156px;background:linear-gradient(160deg,#e8d6c6 0%,#b98c6a 45%,#d85a3a 75%,#f2c23a 100%)}
.cover .band{position:absolute;left:0;top:46px;width:170px;height:80px;background:var(--yellow);padding:20px 10px 0 11px}
.cover .band h1{font-family:"Oswald",sans-serif;font-weight:500;font-size:11px;line-height:11px;color:#222}
.cover .band h1 span{font-family:"Open Sans",sans-serif;font-weight:600;font-size:8px;display:block;margin-top:1px}
.cover .band .welcome{font-size:4.4px;font-weight:700;color:#222;margin-top:6px}
.cover .band .sub{font-size:3px;color:#333}
.cover .lead{position:absolute;left:0;top:126px;width:150px;height:33px;background:#5d5d5d;color:#eee;font-size:3.2px;line-height:4.3px;padding:5px 10px 0 11px}
.cover .strip{position:absolute;left:0;top:162px;width:234px;height:56px;display:flex;gap:2px}
.cover .strip div{flex:1}
.cover .strip .p1{background:linear-gradient(135deg,#6f7f8f,#c7a58a)}
.cover .strip .p2{background:linear-gradient(135deg,#8a6f5a,#d9b08a)}
.cover .strip .p3{background:linear-gradient(135deg,#a07a5c,#e2c49c)}
.cover .labels{position:absolute;left:0;top:218px;width:234px;height:12px;display:flex;gap:2px}
.cover .labels span{flex:1;display:flex;align-items:center;justify-content:center;font-size:4.4px;font-weight:700;color:#222;background:var(--yellow)}
.cover .labels span.mid{background:var(--orange);color:#fff}
.cover .intro{position:absolute;left:0;right:0;top:246px;text-align:center;font-family:"Montserrat",sans-serif;font-weight:400;font-size:10px;color:#333;letter-spacing:.5px}
.cover .cols{position:absolute;left:11px;right:11px;top:268px;display:flex;gap:12px}
.cover .cols p{flex:1;font-size:3.2px;line-height:4.5px;text-align:justify}
.cover .footer{justify-content:center;border-top:none}
.big-mark{position:absolute;left:566px;top:954px;display:flex;align-items:center;gap:10px;font-family:"Open Sans",sans-serif;font-weight:400;font-size:44px;color:#3b3b3b}
.big-mark i{width:28px;height:28px;background:var(--orange);display:block}
</style>
</head>
<body>

<!-- Cover -->
<section class="page cover" style="left:21px;top:22px">
  <div class="portrait" role="img" aria-label="Photo of a smiling student holding colourful folders"></div>
  <div class="logo"><i></i>Kt7up</div>
  <div class="tagline">RESEARCH • POLICY • PRACTICE</div>
  <div class="band">
    <h1>BRVT EDUCATOR TOOLKIT,<span>Research, &amp; Best Practices</span></h1>
    <div class="welcome">Welcome to the BRVT Resource Center</div>
    <div class="sub">View descriptive survey from the Early College High Schools</div>
  </div>
  <div class="lead">Early college high schools use a transformational strategy of bringing college into high school by simultaneously offering a high school diploma and a college-level credential and/or degree.</div>
  <div class="strip">
    <div class="p1" role="img" aria-label="Photo of students working together in class"></div>
    <div class="p2" role="img" aria-label="Photo of a teacher helping students"></div>
    <div class="p3" role="img" aria-label="Photo of students collaborating at a table"></div>
  </div>
  <div class="labels"><span>BRVT Toolkit</span><span class="mid">BRVT Best Practices</span><span>BRVT Collaboration</span></div>
  <div class="intro">INTRODUCTION</div>
  <div class="cols">
    <p>Lorem Ipsum is simply dummy text of the printing and typesetting industry. Lorem Ipsum has been the industry's standard dummy text ever since the 1500s, when an unknown printer took a galley of type and scrambled it to make a type specimen book. It has survived not only five centuries.</p>
    <p>But also the leap into electronic typesetting, remaining essentially unchanged. It was popularised in the 1960s with the release of Typorel sheets containing Lorem Ipsum passages, and more recently with desktop publishing software like Pagewright Studio including versions of Lorem Ipsum.</p>
  </div>
  <div class="footer"><span class="url">www.kt7up.com</span></div>
</section>
<div class="page-label" style="left:21px;top:364px">COVER PAGE</div>

<!-- Page 01 -->
<section class="page" style="left:280px;top:22px">
  <div class="content">
    <div class="section" style="margin-top:4px"><div class="kicker">SECTION 1</div><div class="dots"><i></i><i></i><i></i></div><h2>HISTORY &amp; PURPOSE OF EARLY COLLEGE HIGH SCHOOLS</h2></div>
    <div class="bar">Pressing Problems in Education Led Educators to Seek Strong Solutions</div>
    <p class="t">Many of our high schools, particularly in high-poverty areas, are struggling to help our children:</p>
    <ul class="b"><li>More than half of public school students are from low-income families.</li><li>And nearly half of American high schools do not offer students rigorous coursework.</li></ul>
    <p class="t">We need to develop innovative programs that prepare all students for success in high school, college and careers, particularly as projections show most new jobs will require postsecondary education.</p>
    <p class="t">Over the past decade, education, the economy and workforce readiness have converged to redefine what our students require from schools before high school graduation. Multiple factors led this convergence, and the number of high school graduates enrolling in postsecondary education keeps rising.</p>
    <p class="t">The labor statistics office estimated that most occupations with the highest projected growth will require education beyond high school, and many will require a credential beyond the diploma.</p>
    <p class="t">In light of projections such as these, we need to direct our children to a college education, particularly our low-income students and those whose families have not attended college in the past.</p>
    <p class="t">Other problems emerge as state, district and local educators begin to develop policies for new educational models such as BRVTs.</p>
    <div class="callout">Many students from underserved areas will be the first in their family to attend college. Without college experience, parents may be unsure how to guide their children. Parents themselves may need the support of educators as well.</div>
  </div>
  <div class="footer"><span class="brand"><i></i>Kt7up</span><span class="url">www.kt7up.com</span><span>01</span></div>
</section>
<div class="page-label" style="left:280px;top:364px">PAGE - 01</div>

<!-- Page 02 -->
<section class="page" style="left:539px;top:22px">
  <div class="content">
    <div class="bar" style="margin-top:4px">History and Purpose of Early College High Schools</div>
    <p class="t">The Early College High School (BRVT) model began in 2002 with foundation funding to improve college readiness and completion rates for students underrepresented in postsecondary education.</p>
    <div class="callout">According to a foundation education director, "It's no wonder students drop out. They are shuffled through the system with adults who hardly know them. We need to engage and motivate students by giving them the personalized and rigorous courses they need to make a smooth transition to college or the workplace."</div>
    <p class="t">This new model for high schools came about in response to the need to increase high school graduation rates and equip all students with the skills they need to successfully complete college-level work and meet the needs of today's workplace.</p>
    <p class="t">With the BRVT model, we raise the expectations traditionally underserved and high-risk students have for themselves by offering them access to advanced high school courses and college courses at the same time.</p>
    <p class="t">Several characteristics generally distinguish BRVTs. These include:</p>
    <ul class="b"><li>Their small size, typically with up to 100 students per grade level.</li><li>Responsible growth. BRVTs typically begin in 9th grade and take four years to reach full capacity.</li><li>A close proximity to the postsecondary partner, in some cases directly on the college campus.</li><li>Block scheduling of classes to allow acceleration of graduation requirements so students can take college courses.</li><li>Limited high school electives since most elective credits are earned through dual credit coursework.</li></ul>
    <p class="t">Clearly, the BRVT model makes sense. It assumes students who engage in rigorous coursework in high school are better ready for college-level work and more likely to earn a postsecondary degree.</p>
  </div>
  <div class="footer"><span class="brand"><i></i>Kt7up</span><span class="url">www.kt7up.com</span><span>02</span></div>
</section>
<div class="page-label" style="left:539px;top:364px">PAGE - 02</div>

<!-- Page 03 -->
<section class="page" style="left:21px;top:413px">
  <div class="content">
    <div class="bar" style="margin-top:4px;width:92%">Comparisons of Early College High Schools with Other Dual Credit Programs</div>
    <p class="t">Over the past decades, other "accelerating" programs have been introduced to secondary school students. A short comparison of these with the BRVT model affirms the strength of BRVTs in making a difference in learning and achievement for so many students.</p>
    <p class="t">When comparing dual enrollment programs with BRVTs, it becomes clear BRVTs are a more structured dual enrollment strategy specifically targeted at traditionally underserved students, and one which has demonstrated its effectiveness in increasing postsecondary participation and attainment rates for this high-need population.</p>
    <ul class="b"><li>While dual enrollment programs tend to draw students who are mid- to high-achieving, most students in BRVTs are minority and low-income.</li><li>In dual enrollment, students select individual courses that potentially allow them to earn both high school and postsecondary credit. BRVTs present a cohesive curriculum integrating high school and college-level coursework into a single program.</li></ul>
    <p class="t">A comparison of BRVTs with other advanced programs shows an even more marked difference from the dual enrollment model. While BRVTs set a priority for enrollment on underserved students, other programs do not target a specific population and offer fewer supports to help these students succeed.</p>
    <div class="bar">How Early College High Schools Work</div>
    <p class="t">Early college high schools have the potential to improve high school graduation rates and better prepare students for family-supporting careers by changing the structure of the high school years, reducing the number of years to a college degree, and removing financial and other barriers to college.</p>
    <ul class="b"><li>Starting in 9th or 10th grade, students engage in a curriculum of high school and increasingly postsecondary coursework.</li><li>Depending on the high school, the curricula for both high school and college can be career-focused through Career and Technical Education programs or academies within the school.</li><li>By the end of 12th grade, students who remain in the program will have concurrently earned a high school diploma as well as an associate's degree or up to 60 credit hours of postsecondary coursework.</li></ul>
  </div>
  <div class="footer"><span class="brand"><i></i>Kt7up</span><span class="url">www.kt7up.com</span><span>03</span></div>
</section>
<div class="page-label" style="left:21px;top:755px">PAGE - 03</div>

<!-- Page 04 -->
<section class="page" style="left:280px;top:413px">
  <div class="content">
    <ul class="b" style="margin-top:4px"><li>When students continue their postsecondary education in a four-year university, they enter as a junior.</li></ul>
    <p class="t">The physical site of BRVTs varies, from location on a high school campus in a school-within-a-school format, on a college or university campus, or in a stand-alone BRVT campus. Wherever it is located, BRVT college courses are taught by instructors from the college or university partnering with the high school.</p>
    <p class="t">Because BRVTs serve high-need students, programs need to remain flexible to accommodate challenges students may have to succeed. Examples of this flexibility are shown following:</p>
    <span class="tag">Rigorous curriculum</span>
    <p class="t">Regardless of their background, when students arrive at BRVTs, they are there to learn.</p>
    <ul class="b"><li>Each BRVT sets its own curriculum and pacing to help their students succeed.</li><li>Some BRVTs integrate college courses into the curriculum, but at a slower pace. For example, students advance through high school with no credit-bearing classes in 9th grade, up to 10 credits in 10th grade, and more in the 11th and 12th grades.</li><li>Other BRVTs have developed plans for two years of credit with expectations that only some students will achieve this goal.</li><li>Still other BRVTs have reduced attainment goals for all students.</li></ul>
    <p class="t">In all these programs, the intent is to make the curriculum as rigorous as possible without shutting the door on any student.</p>
    <span class="tag">Alternative pathways</span>
    <ul class="b"><li>Students interested in industry-based careers may want to earn industry-approved certifications in high school rather than prepare for a two- or four-year degree program.</li><li>While these credentials may be more relevant to student interests, they are often less academically rigorous, so that students who are performing at a lower academic level can still achieve high standards of learning.</li></ul>
    <span class="tag">Compressed learning time</span>
    <p class="t">In the BRVT model, students can earn up to six years of work in just four years. This compressed time frame presents obvious opportunities and challenges, particularly for students who are under-prepared entering 9th grade.</p>
    <ul class="b"><li>To reduce these challenges, some BRVTs include a fifth year of high school and build middle-school outreach to get students ready sooner.</li></ul>
  </div>
  <div class="footer"><span class="brand"><i></i>Kt7up</span><span class="url">www.kt7up.com</span><span>04</span></div>
</section>
<div class="page-label" style="left:280px;top:755px">PAGE - 04</div>

<!-- Page 05 -->
<section class="page" style="left:539px;top:413px">
  <div class="content">
    <span class="tag" style="margin-top:6px">Student support</span>
    <p class="t">BRVTs provide strong support systems to assure students can succeed. Examples may include: academic advising, parent involvement and communications, tutoring, review sessions, homework guidance, summer sessions, learning labs, skill development classes, college planning sessions, and college application and funding workshops.</p>
    <span class="tag">Community partnerships</span>
    <p class="t">BRVTs naturally form partnerships with colleges and universities as well as businesses to help students meet their goals and remove financial obstacles associated with earning college credit and/or certifications.</p>
    <div class="bar">Early College High Schools and ESSA</div>
    <p class="t">The Every Student Succeeds Act (ESSA), signed into law in December 2015, reauthorizes the Elementary and Secondary Education Act, the nation's national education law and longstanding commitment to equal opportunity for all students. The BRVT model supports and provides funding for BRVTs in several areas:</p>
    <ul class="b"><li>ESSA requires states to set challenging academic standards in reading/language arts and mathematics that are aligned with:</li></ul>
    <ul class="b sub"><li>Entrance requirements for credit-bearing coursework in a state's system of higher education.</li><li>Relevant state career and technical education standards.</li><li>When implementing BRVTs, districts may target Title I funds to high schools with a poverty rate of 50% or higher.</li></ul>
    <ul class="b"><li>District plans must facilitate effective transitions from high school to postsecondary education through, if applicable:</li></ul>
    <ul class="b sub"><li>Coordination with colleges and universities, employers, and other local partners.</li><li>Increased student access to BRVTs or dual or concurrent enrollment opportunities, or career counseling to identify students' interests and skills.</li></ul>
    <ul class="b"><li>Title II (professional development funding) may be used to provide training on effective strategies to integrate rigorous academic content, career and technical education, and work-based learning, which may include providing common planning time.</li></ul>
  </div>
  <div class="footer"><span class="brand"><i></i>Kt7up</span><span class="url">www.kt7up.com</span><span>05</span></div>
</section>
<div class="page-label" style="left:539px;top:755px">PAGE - 05</div>

<!-- Page 06 -->
<section class="page" style="left:21px;top:807px">
  <div class="content">
    <ul class="b" style="margin-top:4px"><li>Title III (instruction for limited English-proficient and immigrant students funding) may be used to offer BRVT or dual- or concurrent-enrollment programs, or courses designed to help English learners achieve success in postsecondary education.</li><li>Direct Student Services funding may be used to provide for enrollment and participation in academic courses not otherwise available. These include advanced courses and career and technical education coursework that is aligned with challenging state academic standards and leads to industry-recognized credentials.</li></ul>
    <div class="section" style="margin-top:22px"><div class="kicker">SECTION 2</div><div class="dots"><i></i><i></i><i></i></div><h2>THE LANGUAGE OF EARLY COLLEGE HIGH SCHOOLS<br>UNDERSTANDING THE TERMS</h2></div>
    <p class="t">To better understand the BRVTs, it is important to become familiar with some of the basic definitions that distinguish the model.</p>
    <span class="tag">Career and Technical Education (CTE)</span>
    <p class="t">Courses directly related to the preparation of individuals for the employment in current or emerging occupations requiring an industry-recognized credential, certificate or degree.</p>
    <p class="t">While not all BRVTs are CTE programs, most have career pathways or academies through which students earn industry credentials prior to graduation. Other BRVTs may primarily focus on earning college credits in an academic area such as Science, Technology, Engineering, Math (STEM) or computer science.</p>
    <span class="tag">CTE Standards</span>
    <p class="t">Performance standards for students enrolled in career and technical education (CTE) coursework.</p>
    <span class="tag">Dual Credit/Enrollment</span>
    <p class="t">High-school student enrollment in college-level courses offered by a postsecondary institution that allows students to earn credit toward high-school graduation and a postsecondary degree or certificate simultaneously.</p>
  </div>
  <div class="footer"><span class="brand"><i></i>Kt7up</span><span class="url">www.kt7up.com</span><span>06</span></div>
</section>
<div class="page-label" style="left:21px;top:1149px">PAGE - 06</div>

<!-- Page 07 -->
<section class="page" style="left:280px;top:807px">
  <div class="content">
    <span class="tag" style="margin-top:6px">Postsecondary Partner</span>
    <p class="t">Postsecondary educational institution that has an agreement or memorandum of understanding with a BRVT.</p>
    <span class="tag">Pathway</span>
    <p class="t">Sequence of classes at the BRVT in partnership with the postsecondary partner, which leads to a certification, associate's degree, or bachelor's degree.</p>
    <span class="tag">Work-Based Learning</span>
    <p class="t">Activities that provide students with authentic workplace experiences while in high school. These strengthen a student's engagement with their learning, build their understanding of the importance of college, and affirm their commitment to and interest in their chosen careers. Work-based learning includes job shadowing, internships, or youth pre-apprenticeships.</p>
    <span class="tag">Workforce Recognized Credential</span>
    <p class="t">Industry-recognized workforce credentials, certificates, associate's degrees, or bachelor's degrees from a postsecondary partner.</p>
    <span class="tag">Workforce Partner</span>
    <p class="t">Local business, regional workforce investment board, chamber of commerce, economic development corporation, or other industry representative that provides ongoing support and involvement with course development including projects for project-based learning, relevant content, and work skills as well as mentoring and on-the-job experience.</p>
    <div class="section" style="margin-top:14px"><div class="kicker">SECTION 3</div><div class="dots"><i></i><i></i><i></i></div><h2>HOW WELL EARLY COLLEGE HIGH SCHOOLS<br>ARE DOING NATIONWIDE</h2></div>
    <p class="t">Educators are taking heed of the strong outcomes being reported for the BRVT model, particularly for low-income, high-need, and under-represented students. These outcomes are worth noting as more schools consider transitioning from a traditional high school to a BRVT.</p>
  </div>
  <div class="footer"><span class="brand"><i></i>Kt7up</span><span class="url">www.kt7up.com</span><span>07</span></div>
</section>
<div class="page-label" style="left:280px;top:1149px">PAGE - 07</div>

<div class="big-mark"><i></i>Kt7up</div>

</body>
</html>
```